New automotive search style homepage

Looking for someone that can create a new homepage layout for my company. What we currently have is a little plain above the fold. We are an automotive technology company, where we take over the negotiation for customers, and perhaps we can have a design that appeals to that idea more. The current chat container is our only way to search currently, but would love to have a hybrid chat and manual search container, with the manual fields being make and model. This shouldn't have a toggle, but a seamless split view housing both features. You can see current design of our site at motorlane.net

Target Market(s)

Car buyers

Industry/Entity Type

Automotive

Number of Pages Required

1 page

Colors
0054AA
0677BA
7BADD7
CADEEF
E8F1F8

Requirements
Must have
• Above the fold is the most important

```html
<!DOCTYPE html>
<html lang="en">
<head>
<meta charset="utf-8">
<title>MotorLane — Smarter Search. Better Decisions.</title>
<link rel="stylesheet" href="https://fonts.googleapis.com/css2?family=Inter:wght@400;500;600;700;800&display=swap">
<style>
  :root {
    --blue-strong: #0054AA;
    --blue-mid: #0677BA;
    --blue-bright: #1378d6;
    --blue-soft: #7BADD7;
    --blue-pale: #CADEEF;
    --blue-mist: #E8F1F8;
    --navy-deep: #021733;
    --navy: #06285c;
    --navy-panel: #05377f;
    --ink: #0d1b2e;
    --text: #1f2a37;
    --white: #ffffff;
    --section-bg: #f1f6fb;
  }
  * { box-sizing: border-box; margin: 0; padding: 0; }
  html, body { width: 1200px; height: 884px; overflow: hidden; }
  body { font-family: "Inter", sans-serif; color: var(--text); background: var(--white); position: relative; }

  /* Header */
  .site-header { position: absolute; left: 0; top: 0; width: 1200px; height: 69px; background: var(--white); }
  .brand { position: absolute; left: 53px; top: 19px; display: flex; align-items: center; gap: 9px; }
  .brand-mark { width: 30px; height: 30px; background: var(--blue-strong); border-radius: 4px; }
  .brand-name { font-weight: 700; font-size: 25px; color: var(--ink); letter-spacing: -0.3px; }
  .main-nav { position: absolute; left: 467px; top: 0; height: 69px; display: flex; align-items: center; gap: 0; }
  .main-nav a { font-size: 13px; color: var(--ink); text-decoration: none; position: relative; margin-right: 44px; display: flex; align-items: center; gap: 4px; }
  .main-nav a.is-active::after { content: ""; position: absolute; left: 0; right: 0; bottom: -9px; height: 2px; background: var(--blue-bright); }
  .auth { position: absolute; top: 17px; left: 951px; display: flex; gap: 11px; }
  .auth a { height: 35px; border: 1.5px solid var(--ink); border-radius: 18px; font-size: 13px; color: var(--ink); text-decoration: none; display: flex; align-items: center; justify-content: center; gap: 5px; }
  .auth .login { width: 89px; }
  .auth .signup { width: 92px; }

  /* Hero */
  .hero { position: absolute; left: 0; top: 69px; width: 1200px; height: 518px; overflow: hidden;
    background: linear-gradient(90deg, var(--navy-deep) 0%, #03214a 30%, #0b3f86 52%, #2d6cb8 70%, #6f9fd2 85%, #a9c6e6 100%); }
  .hero-scene { position: absolute; left: 520px; top: 0; width: 680px; height: 518px;
    background: radial-gradient(ellipse at 75% 60%, rgba(20,60,130,.85) 0%, rgba(20,60,130,0) 55%),
                linear-gradient(180deg, rgba(255,255,255,0) 55%, rgba(2,23,51,.55) 100%); }
  .eyebrow { position: absolute; left: 57px; top: 49px; font-size: 14px; font-weight: 500; color: var(--blue-bright); letter-spacing: .1px; }
  .hero-title { position: absolute; left: 55px; top: 66px; font-size: 52px; font-weight: 700; line-height: 54px; letter-spacing: -0.5px; color: var(--white); }
  .hero-title .accent { color: var(--blue-bright); display: block; }
  .hero-lead { position: absolute; left: 57px; top: 203px; width: 400px; font-size: 14.5px; line-height: 22.5px; color: var(--white); }

  .search-panel { position: absolute; left: 56px; top: 260px; width: 531px; height: 188px; border-radius: 8px; background: var(--navy-panel); overflow: hidden; }
  .tabs { display: flex; height: 64px; }
  .tab { width: 265px; display: flex; align-items: center; gap: 15px; padding-left: 38px; color: var(--white); }
  .tab + .tab { background: var(--navy); padding-left: 40px; width: 266px; }
  .tab-icon { width: 32px; height: 32px; border-radius: 4px; background: var(--white); display: flex; align-items: center; justify-content: center; flex-shrink: 0; }
  .tab + .tab .tab-icon { background: none; }
  .tab strong { display: block; font-size: 12.5px; font-weight: 700; }
  .tab span { display: block; font-size: 9.5px; margin-top: 4px; }
  .field-label { position: absolute; top: 82px; font-size: 10px; font-weight: 600; color: var(--white); }
  .select { position: absolute; top: 95px; width: 159px; height: 39px; border-radius: 4px; background: var(--white); font-size: 11px; color: #4b5563; display: flex; align-items: center; justify-content: space-between; padding: 0 13px; }
  .search-btn { position: absolute; left: 358px; top: 95px; width: 150px; height: 39px; border-radius: 4px; background: var(--blue-bright); color: var(--white); font-size: 12px; font-weight: 700; display: flex; align-items: center; justify-content: center; }
  .assurance { position: absolute; left: 18px; top: 162px; font-size: 10px; font-weight: 500; color: var(--white); display: flex; align-items: center; gap: 7px; }

  .or-badge { position: absolute; left: 595px; top: 332px; width: 42px; height: 42px; border-radius: 50%; background: var(--blue-bright); color: var(--white); font-size: 14px; font-weight: 700; display: flex; align-items: center; justify-content: center; }

  .chat-panel { position: absolute; left: 644px; top: 260px; width: 365px; height: 188px; border-radius: 8px; background: rgba(236,241,248,.9); }
  .chat-title { position: absolute; left: 19px; top: 21px; font-size: 12.5px; font-weight: 600; color: var(--blue-bright); display: flex; align-items: center; gap: 6px; }
  .chat-hint { position: absolute; left: 19px; top: 59px; width: 323px; height: 53px; border-radius: 5px; background: var(--blue-pale); font-size: 10.5px; line-height: 17.5px; color: var(--text); padding: 8px 12px; }
  .chat-input { position: absolute; left: 19px; top: 130px; width: 283px; height: 36px; border-radius: 4px; background: var(--white); border: 1px solid #dbe3ee; font-size: 11px; color: #6b7280; display: flex; align-items: center; padding-left: 10px; }
  .chat-send { position: absolute; left: 314px; top: 130px; width: 32px; height: 32px; border-radius: 50%; background: var(--blue-strong); display: flex; align-items: center; justify-content: center; }

  /* Features */
  .features { position: absolute; left: 0; top: 587px; width: 1200px; height: 113px; background: var(--white); }
  .feature { position: absolute; top: 32px; display: flex; gap: 12px; }
  .feature-icon { width: 45px; height: 45px; border-radius: 50%; border: 1px solid var(--blue-pale); display: flex; align-items: center; justify-content: center; flex-shrink: 0; margin-top: 1px; }
  .feature h3 { font-size: 12px; font-weight: 700; color: var(--ink); margin-bottom: 4px; margin-top: -2px; }
  .feature p { font-size: 10.5px; line-height: 17.5px; color: var(--text); }
  .divider { position: absolute; top: 33px; width: 1px; height: 47px; background: #dfe5ec; }

  /* Resource intro */
  .resource-intro { position: absolute; left: 0; top: 700px; width: 1200px; height: 184px; background: var(--section-bg); text-align: center; }
  .resource-intro .kicker { margin-top: 26px; font-size: 13px; font-weight: 500; color: var(--blue-bright); letter-spacing: .2px; }
  .resource-intro h2 { margin-top: 10px; font-size: 25px; font-weight: 700; color: var(--ink); }
  .resource-intro p { margin-top: 12px; font-size: 13px; color: var(--text); }
</style>
</head>
<body>

<header class="site-header">
  <div class="brand"><span class="brand-mark"></span><span class="brand-name">MotorLane</span></div>
  <nav class="main-nav">
    <a href="#" class="is-active">Home</a>
    <a href="#">About Us</a>
    <a href="#">Blog</a>
    <a href="#">Tools
      <svg width="9" height="6" viewBox="0 0 9 6"><path d="M1 1l3.5 3.5L8 1" fill="none" stroke="#0d1b2e" stroke-width="1.5"/></svg></a>
    <a href="#">Contact</a>
  </nav>
  <div class="auth">
    <a href="#" class="login">
      <svg width="12" height="13" viewBox="0 0 12 13"><circle cx="6" cy="3.8" r="2.8" fill="none" stroke="#0d1b2e" stroke-width="1.3"/><path d="M1 12.3c0-2.8 2.2-4.5 5-4.5s5 1.7 5 4.5z" fill="none" stroke="#0d1b2e" stroke-width="1.3"/></svg>
      Log In</a>
    <a href="#" class="signup">Sign Up</a>
  </div>
</header>

<section class="hero">
  <div class="hero-scene" role="img" aria-label="Blue sports car driving on a curved highway in front of a city skyline, with glowing data icons floating above"></div>

  <p class="eyebrow">AUTOMOTIVE DATA. AI-POWERED.</p>
  <h1 class="hero-title">Smarter Search.<span class="accent">Better Decisions.</span></h1>
  <p class="hero-lead">Search for any vehicle and get instant access to specs, features, prices, comparisons and more.</p>

  <div class="search-panel">
    <div class="tabs">
      <div class="tab">
        <span class="tab-icon"><svg width="20" height="20" viewBox="0 0 20 20"><circle cx="8.5" cy="8.5" r="6" fill="none" stroke="#0d1b2e" stroke-width="2"/><path d="M13 13l5 5" stroke="#0d1b2e" stroke-width="2.2" stroke-linecap="round"/></svg></span>
        <div><strong>Manual Search</strong><span>Search by Make &amp; Model</span></div>
      </div>
      <div class="tab">
        <span class="tab-icon"><svg width="34" height="32" viewBox="0 0 34 32"><path d="M2 3h22v15H11l-6 5v-5H2z" fill="none" stroke="#2f8ef0" stroke-width="1.8" stroke-linejoin="round"/><path d="M26 10h6v14h-3v5l-6-5H12v-3" fill="none" stroke="#2f8ef0" stroke-width="1.8" stroke-linejoin="round"/><path d="M7 9h12M7 13h9" stroke="#2f8ef0" stroke-width="1.8"/></svg></span>
        <div><strong>AI Chat Search</strong><span>Ask anything about cars</span></div>
      </div>
    </div>
    <span class="field-label" style="left:18px">MAKE</span>
    <span class="field-label" style="left:188px">MODEL</span>
    <div class="select" style="left:18px">Select Make <svg width="10" height="6" viewBox="0 0 10 6"><path d="M1 1l4 4 4-4" fill="none" stroke="#0d1b2e" stroke-width="1.6"/></svg></div>
    <div class="select" style="left:188px">Select Make <svg width="10" height="6" viewBox="0 0 10 6"><path d="M1 1l4 4 4-4" fill="none" stroke="#0d1b2e" stroke-width="1.6"/></svg></div>
    <div class="search-btn">Search Vehicles</div>
    <div class="assurance">
      <svg width="14" height="16" viewBox="0 0 14 16"><path d="M7 1l5.5 2v5c0 3.3-2.4 5.8-5.5 7-3.1-1.2-5.5-3.7-5.5-7V3z" fill="none" stroke="#7BADD7" stroke-width="1.3"/><path d="M4.5 8l2 2 3-3.5" fill="none" stroke="#7BADD7" stroke-width="1.3"/></svg>
      Accurate. Reliable. Up-to-date.</div>
  </div>

  <div class="or-badge">OR</div>

  <div class="chat-panel">
    <div class="chat-title">
      <svg width="22" height="22" viewBox="0 0 22 22"><path d="M9 4l1.8 5.2L16 11l-5.2 1.8L9 18l-1.8-5.2L2 11l5.2-1.8z" fill="none" stroke="#1378d6" stroke-width="1.5" stroke-linejoin="round"/><path d="M17 1l.8 2.2L20 4l-2.2.8L17 7l-.8-2.2L14 4l2.2-.8z" fill="#1378d6"/><path d="M17 16l.6 1.4L19 18l-1.4.6L17 20l-.6-1.4L15 18l1.4-.6z" fill="#1378d6"/></svg>
      Ask our AI about any vehicle</div>
    <div class="chat-hint">Try asking: "Best 3-row SUVs under $40K"<br>or "2024 Arden Coupe vs Velto Sedan"</div>
    <div class="chat-input">Type your question here</div>
    <div class="chat-send"><svg width="16" height="16" viewBox="0 0 16 16"><path d="M15 1L1 7l5 2 2 5z M15 1L6 9" fill="none" stroke="#fff" stroke-width="1.4" stroke-linejoin="round"/></svg></div>
  </div>
</section>

<section class="features">
  <div class="feature" style="left:55px">
    <span class="feature-icon"><svg width="26" height="24" viewBox="0 0 26 24"><rect x="2" y="3" width="22" height="14" rx="1.5" fill="none" stroke="#1378d6" stroke-width="1.4"/><path d="M6 14V10M10 14V7M14 14V9M18 14V6" stroke="#1378d6" stroke-width="1.6"/><path d="M9 21h8M13 17v4" stroke="#1378d6" stroke-width="1.4"/></svg></span>
    <div><h3>Comprehensive Data</h3><p>Access detailed specs, pricing,<br>features and more</p></div>
  </div>
  <span class="divider" style="left:279px"></span>
  <div class="feature" style="left:300px">
    <span class="feature-icon"><svg width="24" height="24" viewBox="0 0 24 24"><circle cx="13" cy="9" r="6" fill="none" stroke="#1378d6" stroke-width="1.4"/><path d="M10 9l2 2 4-4" fill="none" stroke="#1378d6" stroke-width="1.5"/><path d="M2 17l4-2h5l5 2 4-3M2 21l5-1h6" fill="none" stroke="#1378d6" stroke-width="1.4"/></svg></span>
    <div><h3>Trusted &amp; Accurate</h3><p>Our data is verified and<br>updated regularly</p></div>
  </div>
  <span class="divider" style="left:491px"></span>
  <div class="feature" style="left:511px">
    <span class="feature-icon"><svg width="24" height="24" viewBox="0 0 24 24"><rect x="3" y="3" width="8" height="16" rx="1" fill="none" stroke="#1378d6" stroke-width="1.4"/><rect x="14" y="3" width="7" height="9" rx="1" fill="none" stroke="#1378d6" stroke-width="1.4"/><path d="M5 8h4M5 12h4M16 7h3M17 15v6M14 21h6" stroke="#1378d6" stroke-width="1.4"/></svg></span>
    <div><h3>Compare with Confidence</h3><p>Side-by-side comparisons<br>made simple</p></div>
  </div>
  <span class="divider" style="left:728px"></span>
  <div class="feature" style="left:748px">
    <span class="feature-icon"><svg width="24" height="24" viewBox="0 0 24 24"><circle cx="14" cy="9" r="6" fill="none" stroke="#1378d6" stroke-width="1.4"/><path d="M14 6v3l2 2" fill="none" stroke="#1378d6" stroke-width="1.4"/><path d="M2 18l4-3h5l3 2-3 2h-4M11 19l7-3" fill="none" stroke="#1378d6" stroke-width="1.4"/></svg></span>
    <div><h3>Save Time</h3><p>Find the right vehicle<br>faster with AI</p></div>
  </div>
  <span class="divider" style="left:944px"></span>
  <div class="feature" style="left:964px">
    <span class="feature-icon"><svg width="26" height="24" viewBox="0 0 26 24"><rect x="6" y="3" width="16" height="11" rx="1.5" fill="none" stroke="#1378d6" stroke-width="1.4"/><path d="M2 18h4M8 18h16M2 21h6M10 21h14" stroke="#1378d6" stroke-width="1.4"/></svg></span>
    <div><h3>Built for Car Buyers</h3><p>Everything you need to<br>make smarter decisions.</p></div>
  </div>
</section>

<section class="resource-intro">
  <p class="kicker">ALL THE INFORMATION YOU NEED</p>
  <h2>Your One-Stop Automotive Resource</h2>
  <p>From research to comparison, we provide everything you need to find the right vehicle.</p>
</section>

</body>
</html>
```